KW Sports & Remedial Massage needs a new logo & business card design

The design is for my Sports and remedial massage business. My business is aimed at everyone who has a muscle ache or injury so not just sports related. I need a design which is sharp, clear and professional. No greens, or pastel colours or floral/girly designs. Perhaps just a Navy background and white text or other way around or perhaps grey. I want to make it clear that I treat everyone and not just sporty people.

Target Market(s)

People with muscle aches or sports injuries

Industry/Entity Type

Health And Wellness

Contact Information for Business Card

It needs to also include the following:
Name: Marion Kebbell
Mobile No: 07432 519 268
Email: marionkebbell@postvane.com
Qualifications: Dip SM, Dip SRM

Logo Text

KW Sports & Remedial Massage

Font styles to use
Serif
Other font styles liked:
• Tahoma, Verdana

Colors
5c5c5c
7f7f7f
9d9d9d
0255a3
3176b5
85abd2

Requirements
Must have
• I was thinking of a few simple people figures at the bottom of the card to highlight this i.e. a gardener, musician mixed in with a cyclist and tennis player.
Should not have
• Anything which indicates beauty therapy or relaxing. I am there to get rid of aches and pains and often to give rehab to certain injuries.

```html
<!DOCTYPE html>
<html lang="en">
<head>
<meta charset="utf-8">
<title>KW Sports &amp; Remedial Massage – Business Card</title>
<link rel="stylesheet" href="https://fonts.googleapis.com/css2?family=Arimo:wght@400&display=swap">
<style>
  :root {
    --page-bg: #2b2b2b;
    --card-top: #0c0c0e;
    --card-band: #2f4b9d;
    --brand-blue: #3176b5;
    --ink-light: #e9ecf4;
    --ink-soft: #c9d0e6;
    --figure-fill: #e6e8ec;
    --figure-fill-2: #c8ccd6;
  }
  * { box-sizing: border-box; margin: 0; padding: 0; }
  html, body {
    width: 1200px; height: 797px; overflow: hidden;
    background: var(--page-bg);
    font-family: "Arimo", Arial, sans-serif;
  }
  .business-card {
    position: absolute; left: 80px; top: 62px;
    width: 1040px; height: 673px;
    background: var(--card-band);
    border-radius: 6px;
    overflow: hidden;
  }
  .card-top {
    position: absolute; left: 0; top: 0; width: 100%; height: 300px;
    background: var(--card-top);
  }
  .brand-name {
    position: absolute; left: 80px; top: 58px;
    font-size: 50px; font-weight: 400; color: var(--brand-blue);
    letter-spacing: 0.5px; white-space: nowrap;
  }
  .figure {
    position: absolute;
    border-radius: 40px 40px 14px 14px;
    background: linear-gradient(180deg, var(--figure-fill), var(--figure-fill-2));
  }
  .figure--musician { left: 150px; top: 180px; width: 100px; height: 290px; }
  .figure--cyclist  { left: 290px; top: 180px; width: 180px; height: 230px; }
  .figure--tennis   { left: 510px; top: 150px; width: 160px; height: 220px; }
  .figure--gardener { left: 700px; top: 120px; width: 150px; height: 210px; }
  .contact-list {
    position: absolute; right: 70px; top: 410px;
    list-style: none; text-align: right;
  }
  .contact-item {
    display: flex; align-items: center; justify-content: flex-end;
    gap: 22px; font-size: 26px; color: var(--ink-light);
    margin-bottom: 24px; white-space: nowrap;
  }
  .contact-icon { width: 28px; height: 28px; flex: none; }
  .person-name {
    position: absolute; left: 80px; top: 515px;
    font-size: 42px; color: var(--ink-light); font-weight: 400;
  }
  .qualifications {
    position: absolute; left: 86px; top: 572px;
    font-size: 25px; color: var(--ink-soft);
  }
</style>
</head>
<body>
  <article class="business-card">
    <div class="card-top"></div>
    <h1 class="brand-name">KW Sports &amp; Remedial Massage</h1>

    <div class="figure figure--musician" role="img" aria-label="White silhouette of a saxophone player"></div>
    <div class="figure figure--cyclist" role="img" aria-label="White silhouette of a cyclist on a bike"></div>
    <div class="figure figure--tennis" role="img" aria-label="White silhouette of a tennis player swinging a racket"></div>
    <div class="figure figure--gardener" role="img" aria-label="White silhouette of a gardener with a watering can"></div>

    <ul class="contact-list">
      <li class="contact-item">
        <span class="contact-phone">07432 519 268</span>
        <svg class="contact-icon" viewBox="0 0 30 30" aria-hidden="true">
          <rect x="2" y="2" width="26" height="26" rx="3" fill="var(--ink-light)"/>
          <rect x="10" y="6" width="10" height="18" rx="2" fill="none" stroke="var(--card-band)" stroke-width="2"/>
          <rect x="12" y="9" width="6" height="5" fill="var(--card-band)"/>
        </svg>
      </li>
      <li class="contact-item">
        <span class="contact-email">marionkebbell@postvane.com</span>
        <svg class="contact-icon" viewBox="0 0 30 30" aria-hidden="true">
          <rect x="2" y="2" width="26" height="26" rx="3" fill="var(--ink-light)"/>
          <rect x="6" y="9" width="18" height="12" fill="none" stroke="var(--card-band)" stroke-width="2"/>
          <path d="M6 9 L15 16 L24 9" fill="none" stroke="var(--card-band)" stroke-width="2"/>
        </svg>
      </li>
    </ul>

    <h2 class="person-name">Marion Kebbell</h2>
    <p class="qualifications">Dip SM, Dip SRM</p>
  </article>
</body>
</html>
```